Nimbrel Computer Solutions
Business Technology Consulting
Professional
Gerald Pinto
1837 NE 41st Court
Harlow Springs, FL 33987
gerald@nimbrelcs.com
www.nimbrelcs.com
My company file logo. Please contact me if another format is needed.

```html
<!DOCTYPE html>
<html lang="en">
<head>
<meta charset="utf-8">
<title>Nimbrel Computer Solutions – Business Card</title>
<link href="https://fonts.googleapis.com/css2?family=Arimo:wght@400;700&display=swap" rel="stylesheet">
<style>
  :root {
    --backdrop: #3b3b3d;
    --card-white: #ffffff;
    --navy: #1c2f63;
    --navy-deep: #13224d;
    --accent: #c9a646;
    --text-light: #e6ebf5;
  }
  * { margin: 0; padding: 0; box-sizing: border-box; }
  html, body {
    width: 1200px;
    height: 637px;
    overflow: hidden;
    background: var(--backdrop);
    font-family: "Arimo", Arial, sans-serif;
  }
  .stage { position: relative; width: 1200px; height: 637px; }
  .card {
    position: absolute;
    top: 173px;
    width: 547px;
    height: 374px;
    border-radius: 16px;
    background: var(--card-white);
    overflow: hidden;
    box-shadow: 0 6px 18px rgba(0, 0, 0, 0.35);
  }
  .card--front { left: 34px; }
  .card--back { left: 600px; }
  .card__band {
    position: absolute;
    inset: 0;
    width: 100%;
    height: 100%;
  }
  .brand {
    position: absolute;
    display: flex;
    align-items: center;
    gap: 12px;
    color: var(--navy);
    font-weight: 700;
  }
  .brand__dot {
    width: 58px;
    height: 58px;
    border-radius: 50%;
    background: var(--navy);
    flex: none;
  }
  .brand__name { display: flex; flex-direction: column; line-height: 1; }
  .brand__primary { font-size: 46px; letter-spacing: 1px; text-transform: uppercase; }
  .brand__secondary { font-size: 12px; letter-spacing: 3px; text-transform: uppercase; margin-top: 5px; }
  .card--front .brand { left: 36px; top: 16px; }
  .card--back .brand { left: 50%; top: 50%; transform: translate(-50%, -50%); }
  .holder-name {
    position: absolute;
    left: 70px;
    top: 242px;
    color: var(--card-white);
    font-size: 30px;
    font-weight: 700;
  }
  .contact {
    position: absolute;
    left: 317px;
    top: 200px;
    list-style: none;
    color: var(--text-light);
    font-size: 15px;
    line-height: 18px;
  }
</style>
</head>
<body>
  <main class="stage">
    <section class="card card--front" aria-label="Business card front">
      <svg class="card__band" viewBox="0 0 547 374" preserveAspectRatio="none" aria-hidden="true">
        <path d="M0,150 C160,135 330,170 547,150" fill="none" stroke="var(--accent)" stroke-width="4"/>
        <path d="M0,165 C160,150 330,185 547,165 L547,374 L0,374 Z" fill="var(--navy)"/>
      </svg>
      <div class="brand">
        <span class="brand__dot"></span>
        <span class="brand__name">
          <span class="brand__primary">Nimbrel</span>
          <span class="brand__secondary">Computer Solutions</span>
        </span>
      </div>
      <h1 class="holder-name">Gerald Pinto</h1>
      <ul class="contact">
        <li>1837 NE 41st Court</li>
        <li>Harlow Springs, FL 33987</li>
        <li>Phone: 239-555-0147</li>
        <li>Email: gerald@nimbrelcs.com</li>
        <li>Web: www.nimbrelcs.com</li>
      </ul>
    </section>

    <section class="card card--back" aria-label="Business card back">
      <div class="brand">
        <span class="brand__dot"></span>
        <span class="brand__name">
          <span class="brand__primary">Nimbrel</span>
          <span class="brand__secondary">Computer Solutions</span>
        </span>
      </div>
    </section>
  </main>
</body>
</html>
```